Wordpress Design Project - Leadership Mentor Nest

Website Brief

We are looking to have a design produced for a modern professional website. A mind map of the site can be found here: http://www.plorvex.example/view.htm?m=48210573b991c2e7f0d4a6b83f5e1c92

Each of the green tabs are pages just next to them is a very small green globe. If you click this. It will take you through to an example page for that section.

Task description
The website will be made up of:
1. A homepage (this will be the blog see http://www.tessandrabilk.example for an example of the crisp and cleanness we are looking for)
2. A page that will have just a video and option page (see: http://gqtwacademy.example/ for example)
3. 3 pages all with the same structure. (see: http://gqtwacademy.example/zp71kqv20mxe/ for an example). Each will have:
a. A video
b. Tabs at the top of the video that link to the 3 videos and the sales page
c. Link to a resource download
d. Facebook Comments section
4. 2 Page with about the experts and about our company (same style for both)
5. A page that will have a long well designed sales page (see: http://gqtwacademy.example/early-enrollment-2013/ for an example)
6. A page with testimonials on it (see http://www.tessandrabilk.example/praise/)
7. A page that will describe the products, services and provision we will be offering
8. A page that will detail our involvement with charities and not for profits

Must Have
Edgey, crisp design, similar to Tessa Bilkans. We would like the colours to match very well throughout the site and have a unique font (possibly manksans). We want it to have very clean integrations between copy and images with shadows on videos for example like with Tessandrabilks page. We really love this design and would like this to be the inspiration for our site however it would need to certainly have a more executive feel to suit our target market.

We like the idea of some kind of circles, crisp clean lines, nice white space, simple design, corporate looking, communicates wealth/success/massive value. Based on the two logos of QPLTN and the Hub (see attached)

Target Market:
The target market includes intelligent, productive coaches, who are self employed or part of small firms. They are well educated, well read, socially conscious, and committed to making a profound difference with their clients...skilled at the actions of coaching, but not the business side. There will be a ratio of approximately 60% male / 40% female (really? The coaching industry is predominantly female, no?), with an age range of 40 to 60 years. English is our core language. Most will have secondary education and the salary range will be $90,000 to $400,000. We will have a global audience reach, although the primary markets will be North America, Europe and Australia/NZ.

Marketing Objective:
LMN will be an on-line resource for Executive Coaches. The intent of the design will be to present LMN to the world as a highly professional organization. The intent is not to characterize LMN as solely corporate, but will also incorporate elements of entrepreneurialism. We require the brand to incorporate these values:
• Trustworthy – you can trust us
• Professional – we are true professionals whose mission is to provide value to our clients
• Caring - Interested in our clients wellbeing – we are keenly interested in helping our clients build their knowledge, skills, and attitudes to be highly productive and successful
• Successful
• Knowledgeable – we have breadth and depth of knowledge in leadership
• World-class – we have a world-wide target market and, as such, need the brand to reflect a powerful and inclusive image
• Positive Energy - I would like the brand to have positive energy and very clean feng shui
• Prestige
• Massive Value
• Accessible
• Worldly/ Sophisticated
• Affordable
• Mission-critical

Details about the needs, wants, aspirations etc. of our target market
Executive coaches need a process and a system for creating opportunities to do the work they love with clients who are qualified to engage them and pay them. There is a scarcity mentality around their own finances, but ironically an abundance mentality for what's possible in the world and for their clients. They want to make a difference, they want to facilitate transformation, they want to be of deep service.

They aspire to make a decent living doing it! They need help bridging the gap between practitioner/service provider and financially successful entrepreneur/business owner/ leader. They also aspire to have it be easy, as it feels hard for them to generate the revenues they want to generate solely through coaching, so many turn to training, speaking, and other revenue streams.

Required assets to send through to web designer
1. Three blog posts. Each will have:
a. A video/audio
b. Summary of the points raised
c. Download (possibly slides)
2. A page that will have just a video and option page
a. Headline
b. Video
c. One paragraph summary of what we do
3. 3 launch videos. Here for each we will need
a. A video scripted and produced
b. Title for each
c. A resource download
4. Sales page
a. Video
b. Copy
i. Overview
ii. Content of course
iii. Guarentee
iv. Details of bonuses
v. Details of support
vi. Pricing broken down ($30,000 value = $2000)
c. Animated Gif
5. About the company and experts
a. Description of our company, it's vision, mission, purpose and core values.
b. Description of each of us,
i. our key facts and wows,
ii. a picture of us
iii. some interesting facts (giving personality)
iv. Lower down we will add in "Faculty" these will be any thought leaders we invite in to be part of the value delivery (will add to our credibility having such a strong team behind the project)
6. Testimonials
a. Testimonials from coaches from working with us
7. Products, services and provision we will be offering
a. A simple description of each of the key products/services we will be offering
i. Leadership Mentor Sales
ii. Leadership Mentor Marketing
iii. Leadership Mentor Help
iv. Leadership Mentor Mastermind
v. Leadership Mentor Resources
a. List of the various charity work each of us have been involved with

Requirements
Must have
• Edgey, crisp design, similar to Tessa Bilkans. We would like the colours to match very well throughout the site and have a unique font (possibly manksans). We want it to have very clean integrations between copy and images with shadows on videos for example like with Tessandrabilks page. We really love this design and would like this to be the inspiration for our site however it would need to certainly have a more executive feel to suit our target market.

```html
<!DOCTYPE html>
<html lang="en">
<head>
<meta charset="utf-8">
<title>Leadership Mentor Nest</title>
<link rel="stylesheet" href="https://fonts.googleapis.com/css2?family=Ubuntu:wght@400;500&family=Open+Sans:ital,wght@0,400;0,600;0,700;1,400&display=swap">
<style>
:root{
  --orange:#f29422;
  --orange-deep:#ec7c12;
  --heading-orange:#e2692c;
  --green:#3e9a1d;
  --green-light:#8cc63f;
  --green-dark:#4f8f1c;
  --ink:#333333;
  --text:#555555;
  --muted:#8a8a8a;
  --line:#e2e2e2;
  --page-bg:#f1f1f1;
  --panel:#f6f6f6;
  --dark:#3a3a3a;
  --footer:#353535;
  --white:#ffffff;
}
*{box-sizing:border-box;margin:0;padding:0}
html,body{width:1200px;height:2362px;overflow:hidden}
body{background:var(--page-bg);font-family:"Open Sans",Arial,sans-serif;color:var(--text)}
.page{position:relative;width:1200px;height:2362px;overflow:hidden}
.abs{position:absolute}
h1,h2,h3,.brand,.nav a,.tab-title{font-family:"Ubuntu",Arial,sans-serif;font-weight:400}

/* header */
.header{left:0;top:0;width:1200px;height:178px;background:var(--white);border-top:4px solid #d9d9d9}
.brand{left:66px;top:138px;font-size:20px;color:#8a8a8a;letter-spacing:.2px;display:flex;align-items:center;gap:10px}
.brand-dot{width:14px;height:14px;border-radius:50%;background:var(--orange)}
.search{left:879px;top:72px;width:242px;height:32px;border:1px solid #dcdcdc;border-radius:3px;background:#fff;font-size:12px;color:#999;padding:7px 12px}
.search svg{position:absolute;right:10px;top:8px}
.nav{left:484px;top:136px;display:flex;font-size:17px}
.nav a{color:#444;text-decoration:none;padding:0 18px;border-left:1px solid #bbb;line-height:22px}
.nav a:first-child{border-left:none}

/* hero */
.hero{left:0;top:178px;width:1200px;height:436px;background:linear-gradient(180deg,var(--orange),var(--orange-deep))}
.hero-panel{left:57px;top:0;width:1083px;height:436px;background:linear-gradient(90deg,#ffffff 0%,#f7f7f7 35%,#eef1f4 100%)}
.hero-photo{left:389px;top:0;width:691px;height:436px;background:radial-gradient(ellipse at 60% 45%,#c9a58b 0%,#a98470 25%,#dfe3e8 60%,#f3f4f6 100%)}
.hero-title{left:47px;top:92px;font-size:30px;color:var(--heading-orange)}
.hero-sub{left:47px;top:132px;width:420px;font-size:19px;line-height:28px;color:var(--green)}
.hero-text{left:47px;top:206px;width:380px;font-size:12.5px;line-height:21px;color:#555}
.btn-green{background:linear-gradient(180deg,var(--green-light),var(--green-dark));color:#fff;border-radius:3px;text-align:center;font-size:14px;font-weight:600;box-shadow:0 1px 2px rgba(0,0,0,.25)}
.hero-btn{left:47px;top:263px;width:137px;height:35px;line-height:35px;text-transform:uppercase;font-size:14px}
.dots{left:55px;top:385px;display:flex;gap:5px}
.dots span{width:11px;height:11px;border-radius:50%;background:#c4c4c4}

/* content */
.content{left:54px;top:633px;width:1085px;height:1572px;background:var(--white)}
.col-rule{left:769px;top:633px;width:1px;height:1560px;background:var(--line)}
.h-main{font-size:23px;color:var(--ink)}
.copy{font-size:12.5px;line-height:21px;color:var(--text)}
.rule{height:1px;background:var(--line)}
.photo{box-shadow:0 1px 3px rgba(0,0,0,.3)}
.post-title{font-size:12.5px;font-weight:700;color:#444}
.learn{font-size:12px;color:#333;text-transform:uppercase;display:flex;align-items:center;gap:5px}
.share{display:flex;gap:8px;align-items:center;font-size:11px;color:#333}
.share .chip{border:1px solid #c8c8c8;border-radius:2px;background:linear-gradient(#fff,#ececec);padding:1px 7px;height:20px;line-height:17px}
.share .count{border:1px solid #ccc;background:#fff;padding:1px 6px;height:20px;line-height:17px;border-radius:2px}

/* sidebar */
.form-box{left:805px;top:636px;width:321px;height:414px;background:var(--panel);border-radius:3px;box-shadow:0 0 4px rgba(0,0,0,.1)}
.tab-title{left:797px;top:647px;width:305px;height:44px;background:linear-gradient(#4a4a4a,#2e2e2e);color:#fff;font-size:20px;line-height:44px;padding-left:25px}
.tab-fold{left:797px;top:691px}
.label{font-size:11.5px;color:#555}
.input{background:#fff;border:1px solid #cfcfcf;border-radius:3px;box-shadow:inset 0 1px 2px rgba(0,0,0,.08)}
.submit{left:828px;top:1002px;width:107px;height:30px;line-height:30px;font-size:12px}
.res-box{left:805px;top:1066px;width:321px;height:156px;background:var(--panel);border-radius:3px;box-shadow:0 0 4px rgba(0,0,0,.1)}
.res-title{left:829px;top:1084px;font-size:20px;color:var(--ink)}
.res-text{left:829px;top:1113px;width:290px;font-size:12px;line-height:20px;color:#555}
.res-btn{left:830px;top:1162px;width:189px;height:37px;line-height:37px;font-size:15px;font-weight:400;color:#1f3d08}
.h-side{font-size:21px;color:var(--ink)}
.quote-mark{font-family:Georgia,serif;font-size:40px;color:#cfcfcf;line-height:1}
.t-photo{background:#fff;border:1px solid #ddd;box-shadow:0 1px 3px rgba(0,0,0,.2);padding:4px}
.t-photo div{width:100%;height:100%}
.t-text{font-size:11.5px;line-height:20px;font-style:italic;color:#555}
.t-author{font-size:12px;font-weight:700;color:#333}

/* footer */
.footer{left:0;top:2225px;width:1200px;height:137px;background:var(--footer);border-top:3px solid #222}
.foot-nav{left:71px;top:2256px;display:flex;gap:0;font-size:14px;color:#ddd}
.foot-nav span{position:absolute;white-space:nowrap}
.copyright{left:71px;top:2295px;font-size:11px;color:#aaa}
.connect{left:958px;top:2243px;font-size:13px;color:#eee}
.social{left:958px;top:2270px;display:flex;gap:10px}
.social span{width:28px;height:28px;border-radius:50%}
</style>
</head>
<body>
<div class="page">

  <header class="abs header">
    <div class="abs brand"><span class="brand-dot"></span>LeadershipMentorNest.com</div>
    <div class="abs search">Search here..
      <svg width="16" height="16" viewBox="0 0 16 16"><circle cx="6.5" cy="6.5" r="5" fill="none" stroke="#888" stroke-width="1.8"/><line x1="10.2" y1="10.2" x2="14.5" y2="14.5" stroke="#888" stroke-width="2"/></svg>
    </div>
    <nav class="abs nav"><a>Home</a><a>About</a><a>Work With Us</a><a>Testimonials</a><a>Giving Back</a><a>Contact</a></nav>
  </header>

  <section class="abs hero">
    <div class="abs hero-panel">
      <div class="abs hero-photo" role="img" aria-label="Group of smiling business professionals in suits and office wear"></div>
      <h1 class="abs hero-title">Welcome to Leadership Mentor Nest</h1>
      <p class="abs hero-sub">Lorem ipsum dolor sit amet, consectetuer adipiscing elit. Nam cursus.</p>
      <p class="abs hero-text">Praesent vitae lacus. Ut velit enim, vestibulum non, fermentum nec, hendrerit quis, leo. Pellentesque rutrum.</p>
      <div class="abs btn-green hero-btn">Learn More</div>
      <div class="abs dots"><span></span><span></span><span></span><span></span></div>
    </div>
  </section>

  <main class="abs content"></main>
  <div class="abs col-rule"></div>

  <h2 class="abs h-main" style="left:88px;top:647px">Welcome to Our Website Mainpage</h2>
  <p class="abs copy" style="left:88px;top:684px;width:660px">Lorem ipsum dolor sit amet, consectetuer adipiscing elit. Nam cursus. Morbi ut mi. Nullam enim leo, egestas id, condimentum at, laoreet mattis, massa. Sed eleifend nonummy diam.</p>
  <p class="abs copy" style="left:88px;top:741px;width:660px">Praesent mauris ante, elementum et, bibendum at, posuere sit amet, nibh. Duis tincidunt lectus quis dui viverra vestibulum. Suspendisse vulputate aliquam dui. Nulla elementum dui ut augue. Aliquam vehicula mi at mauris. Maecenas placerat, nisl at consequat rhoncus, sem nunc gravida justo, quis eleifend arcu velit quis lacus. Morbi magna magna, tincidunt a, mattis non, imperdiet vitae, tellus. Sed odio est, auctor ac, sollicitudin in, consequat vitae, orci. Fusce id felis. Vivamus sollicitudin metus eget eros.</p>
  <div class="abs rule" style="left:88px;top:866px;width:681px"></div>

  <h2 class="abs h-main" style="left:90px;top:889px;font-size:22px">Recent Blog Post</h2>

  <!-- post 1 -->
  <div class="abs photo" role="img" aria-label="Businessman presenting to a colleague at a meeting table" style="left:90px;top:928px;width:516px;height:214px;background:linear-gradient(120deg,#b8322f 0%,#7a2a22 40%,#3a3a3a 70%,#caa68a 100%)"></div>
  <p class="abs post-title" style="left:90px;top:1153px">Praesent mauris ante, elementum et, bibendum at, posuere sit amet, nibh.</p>
  <p class="abs copy" style="left:90px;top:1179px;width:656px">Duis tincidunt lectus quis dui viverra vestibulum. Suspendisse vulputate aliquam dui. Nulla elementum dui ut augue. Aliquam vehicula mi at mauris. Maecenas placerat, nisl at consequat rhoncus, sem nunc gravida justo, quis eleifend arcu velit quis lacus. Morbi magna magna, tincidunt a, mattis non, imperdiet vitae, tellus. Sed odio est, auctor ac, sollicitudin in, consequat vitae, orci. Fusce id felis. Vivamus sollicitudin metus eget eros.</p>
  <div class="abs learn" style="left:90px;top:1282px">Learn More <svg width="6" height="8"><path d="M0 0L6 4L0 8Z" fill="#333"/></svg></div>
  <div class="abs share" style="left:490px;top:1280px"><span class="chip">Like</span><span class="count">162</span><span class="chip">Share</span><span class="count">195</span><span class="chip">+1</span><span class="count">4</span></div>
  <div class="abs rule" style="left:90px;top:1323px;width:656px"></div>

  <!-- post 2 -->
  <div class="abs photo" role="img" aria-label="Smiling businesswoman with colleagues at a whiteboard" style="left:90px;top:1358px;width:517px;height:214px;background:linear-gradient(100deg,#e9d2a6 0%,#f2efe9 35%,#e5e2de 60%,#2b2b2b 85%,#1d1d1d 100%)"></div>
  <p class="abs post-title" style="left:90px;top:1583px">Praesent mauris ante, elementum et, bibendum at, posuere sit amet, nibh.</p>
  <p class="abs copy" style="left:90px;top:1609px;width:656px">Duis tincidunt lectus quis dui viverra vestibulum. Suspendisse vulputate aliquam dui. Nulla elementum dui ut augue. Aliquam vehicula mi at mauris. Maecenas placerat, nisl at consequat rhoncus, sem nunc gravida justo, quis eleifend arcu velit quis lacus. Morbi magna magna, tincidunt a, mattis non, imperdiet vitae, tellus. Sed odio est, auctor ac, sollicitudin in, consequat vitae, orci. Fusce id felis. Vivamus sollicitudin metus eget eros.</p>
  <div class="abs learn" style="left:90px;top:1712px">Learn More <svg width="6" height="8"><path d="M0 0L6 4L0 8Z" fill="#333"/></svg></div>
  <div class="abs share" style="left:490px;top:1710px"><span class="chip">Like</span><span class="count">162</span><span class="chip">Share</span><span class="count">195</span><span class="chip">+1</span><span class="count">4</span></div>
  <div class="abs rule" style="left:90px;top:1753px;width:656px"></div>

  <!-- post 3 -->
  <div class="abs photo" role="img" aria-label="Business team in suits giving thumbs up" style="left:91px;top:1792px;width:517px;height:215px;background:linear-gradient(180deg,#f4f4f4 0%,#e8e8e8 35%,#3b3b3b 60%,#262626 100%)"></div>
  <p class="abs post-title" style="left:90px;top:2019px">Praesent mauris ante, elementum et, bibendum at, posuere sit amet, nibh.</p>
  <p class="abs copy" style="left:90px;top:2045px;width:656px">Duis tincidunt lectus quis dui viverra vestibulum. Suspendisse vulputate aliquam dui. Nulla elementum dui ut augue. Aliquam vehicula mi at mauris. Maecenas placerat, nisl at consequat rhoncus, sem nunc gravida justo, quis eleifend arcu velit quis lacus. Morbi magna magna, tincidunt a, mattis non, imperdiet vitae, tellus. Sed odio est, auctor ac, sollicitudin in, consequat vitae, orci. Fusce id felis. Vivamus sollicitudin metus eget eros.</p>
  <div class="abs learn" style="left:90px;top:2147px">Learn More <svg width="6" height="8"><path d="M0 0L6 4L0 8Z" fill="#333"/></svg></div>
  <div class="abs share" style="left:490px;top:2145px"><span class="chip">Like</span><span class="count">162</span><span class="chip">Share</span><span class="count">195</span><span class="chip">+1</span><span class="count">4</span></div>
  <div class="abs rule" style="left:90px;top:2189px;width:656px"></div>

  <!-- option form -->
  <div class="abs form-box"></div>
  <div class="abs tab-title">Fill Our Option Form</div>
  <svg class="abs tab-fold" width="9" height="9"><path d="M0 0H9V9Z" fill="#1c1c1c"/></svg>
  <span class="abs label" style="left:825px;top:704px">Full Name:</span>
  <div class="abs input" style="left:825px;top:723px;width:271px;height:29px"></div>
  <span class="abs label" style="left:825px;top:761px">Email address:</span>
  <div class="abs input" style="left:825px;top:780px;width:271px;height:29px"></div>
  <span class="abs label" style="left:825px;top:819px">Phone no:</span>
  <div class="abs input" style="left:825px;top:839px;width:271px;height:29px"></div>
  <span class="abs label" style="left:825px;top:882px">Message</span>
  <div class="abs input" style="left:825px;top:901px;width:271px;height:88px"></div>
  <div class="abs btn-green submit">Submit Now</div>

  <!-- resource -->
  <div class="abs res-box"></div>
  <h3 class="abs res-title">Resource Download</h3>
  <p class="abs res-text">Praesent vitae lacus. Ut velit enim, vestibulum non, fermentum nec, hendrerit quis.</p>
  <div class="abs btn-green res-btn">DOWNLOAD NOW</div>

  <!-- video -->
  <h3 class="abs h-side" style="left:805px;top:1250px">Our Video</h3>
  <div class="abs photo" role="img" aria-label="Video still of a businesswoman in a library office" style="left:805px;top:1287px;width:321px;height:216px;background:linear-gradient(90deg,#6b4a35 0%,#b89a7a 35%,#e6e1da 60%,#f0eeeb 100%)"></div>
  <svg class="abs" style="left:935px;top:1360px" width="60" height="60" viewBox="0 0 60 60"><circle cx="30" cy="30" r="27" fill="rgba(255,255,255,.25)" stroke="#111" stroke-width="4"/><path d="M24 18L42 30L24 42Z" fill="#111"/></svg>

  <!-- testimonials -->
  <h3 class="abs h-side" style="left:805px;top:1560px">Testimonial</h3>

  <span class="abs quote-mark" style="left:795px;top:1604px">&ldquo;</span>
  <div class="abs t-photo" style="left:825px;top:1606px;width:87px;height:76px"><div role="img" aria-label="Portrait of a smiling woman" style="background:linear-gradient(135deg,#d8d8d8,#9a9a9a)"></div></div>
  <p class="abs t-text" style="left:928px;top:1601px;width:180px">Nunc tempus felis vitae urna. Vivamus porttitor, neque at volut-pat rutrum, purus nisi eleifend libero, a tempus libero lectus</p>
  <p class="abs t-text" style="left:823px;top:1690px;width:290px">Morbi eget arcu. Morbi porta, libero id ullamcorper nonummy, nibh ligula pulvinar metus <span style="color:#ccc;font-style:normal;font-family:Georgia,serif;font-size:18px">&rdquo;</span></p>
  <p class="abs t-author" style="left:825px;top:1743px">By Author Name</p>

  <span class="abs quote-mark" style="left:802px;top:1796px">&ldquo;</span>
  <div class="abs t-photo" style="left:840px;top:1798px;width:80px;height:76px"><div role="img" aria-label="Portrait of a young man" style="background:linear-gradient(135deg,#e6c4a8,#b08466)"></div></div>
  <p class="abs t-text" style="left:934px;top:1793px;width:180px">Nunc tempus felis vitae urna. Vivamus porttitor, neque at volut-pat rutrum, purus nisi eleifend libero, a tempus libero lectus</p>
  <p class="abs t-text" style="left:830px;top:1882px;width:290px">Morbi eget arcu. Morbi porta, libero id ullamcorper nonummy, nibh ligula pulvinar metus <span style="color:#ccc;font-style:normal;font-family:Georgia,serif;font-size:18px">&rdquo;</span></p>
  <p class="abs t-author" style="left:831px;top:1935px">By Author Name</p>

  <span class="abs quote-mark" style="left:802px;top:1990px">&ldquo;</span>
  <div class="abs t-photo" style="left:835px;top:1992px;width:85px;height:76px"><div role="img" aria-label="Portrait of a woman with glasses" style="background:linear-gradient(135deg,#c79a7a,#5a3a2a)"></div></div>
  <p class="abs t-text" style="left:934px;top:1987px;width:180px">Nunc tempus felis vitae urna. Vivamus porttitor, neque at volut-pat rutrum, purus nisi eleifend libero, a tempus libero lectus</p>
  <p class="abs t-text" style="left:830px;top:2076px;width:290px">Morbi eget arcu. Morbi porta, libero id ullamcorper nonummy, nibh ligula pulvinar metus <span style="color:#ccc;font-style:normal;font-family:Georgia,serif;font-size:18px">&rdquo;</span></p>
  <p class="abs t-author" style="left:831px;top:2129px">By Author Name</p>

  <!-- footer -->
  <footer class="abs footer"></footer>
  <div class="abs foot-nav" style="left:0;top:2256px">
    <span style="left:71px">About</span>
    <span style="left:146px">Work With Us</span>
    <span style="left:274px">Testimonials</span>
    <span style="left:391px">Giving Back</span>
    <span style="left:498px">Contact</span>
  </div>
  <p class="abs copyright">&copy; 2012 Company Name,&nbsp; All right reserved.&nbsp; Term of use</p>
  <p class="abs connect">Get Connected</p>
  <div class="abs social">
    <span style="background:#4f6ea8"></span>
    <span style="background:#3fa9dc"></span>
    <span style="background:#d8d8d8"></span>
    <span style="background:#cfd6dc"></span>
    <span style="background:#f08a1c"></span>
  </div>

</div>
</body>
</html>
```